BrightLoop (1 page) homepage re-design

Our homepage needs a face-lift! We need our homepage on our website re-designed with a fresh and current look and feel. We have all the details, colour codes and a rough wireframe ready, but need a talented designer to put some personality into our ideas.

What we do: BrightLoop is a digital marketing agency with offices in Australia (Sydney) and South Africa (Cape Town). We specialise in SEO, PPC (otherwise known as Zentro PayLine or SEM), content marketing and Zentro Tallyboard. We use these tools to help our clients realise their business dreams.

VISUAL

Style / theme of the design:
Clean, simplistic, fun, flow.

Websites we draw inspiration from:
This is the theme we want to use to build the website
http://demo.vormalayouts.example/vl/?theme=Pebbled
Inspiration:
https://www.ondrapromo.example/
https://www.nelvagrowth.example.au/
https://quimbel.example.au/
https://torvin.layout-works.example/forum/

What we like about the site:
Clean, simple design, good use of white space. The subtle changing background colours, strong contrast with text. Not too busy or distracting.

What we don’t want: Too many different colours.

Target Market(s)

Our target audience: Marketing Managers of small to medium size businesses in Australia.

Industry/Entity Type

Marketing

Number of Pages Required

1 page

Font styles to use
Sans Serif

Requirements
Must have
• Elements to be added on homepage in order and as seen in attachments:
• - Section 1: Video with team as image and a play button add the heading: We help smart marketing managers achieve their KPIs [line break] and reduce their digital marketing overwhelm.
• - Section 2: Solutions section with the 6 solutions displayed in a row.
• - Section 3: Register Free Webinar with video
• - Section 4: Please add 3 case studies (as seen in attached docs there is only 1 but please add 3 below each other)
• - Section 5: Clients. Please add all client logo’s (black and white)
• - Section 6: Our Blog (as seen attached)
• - Section 7: Conferences Attended (please add the title and a paragraph of lorem Ipsom below) and then please add all conference logo’s attached below.
• - Section 8: In The Media (please add all logo’s titled media) white background
• - Section 9: Footer (dark grey footer) add our Zentro honoured affiliate logo here please
• - Section10: Footer - include:
• - Social logos (WorkMesh, Blipster, Pallwall, ReelDrop, Zentro Hub)
• - Navigation
• - Contact details (name, address, phone number, email)
• Colour codes:
• We want to use light greys, white and charcoal grey for the backgrounds with a pop of our green colour to bring out our branding and all CTA’s to be orange, colour codes below:
• Light grey: #F2F2F2
• Charcoal grey: #161616
• Green: #428E29
• CTA’s: #de7532
• PLEASE NOTE: Please see attached pdf titled: homepagecopybrief.pdf for all the titles and statistics that need to go on the homepage
Should not have
• Too much colour, icons should not be different colours

```html
<!DOCTYPE html>
<html lang="en">
<head>
<meta charset="utf-8">
<title>BrightLoop – Homepage</title>
<link rel="stylesheet" href="https://fonts.googleapis.com/css2?family=Montserrat:wght@400;500;600;700&family=Open+Sans:wght@400;600;700&display=swap">
<style>
:root{
  --light:#f2f2f2;
  --charcoal:#161616;
  --green:#428e29;
  --cta:#de7532;
  --text:#333333;
  --muted:#777777;
  --line:#dddddd;
  --white:#ffffff;
}
*{box-sizing:border-box;margin:0;padding:0}
html,body{width:1200px;height:4235px;overflow:hidden}
body{position:relative;background:var(--white);font-family:"Open Sans",Arial,sans-serif;color:var(--text)}
.abs{position:absolute}
.heading{font-family:"Montserrat",Arial,sans-serif;font-weight:500;color:var(--charcoal);font-size:34px;letter-spacing:.5px;text-align:center;width:1200px;left:0}
.heading::after{content:"";display:block;width:40px;height:2px;background:var(--cta);margin:14px auto 0}
.lead{font-size:12.5px;line-height:22px;text-align:center;color:var(--charcoal);width:560px;left:320px}
.btn{display:flex;align-items:center;justify-content:center;background:var(--cta);color:var(--white);font-family:"Montserrat",Arial,sans-serif;font-weight:600;font-size:12px;letter-spacing:.5px;border-radius:20px;text-transform:uppercase}

/* hero */
.hero{left:0;top:0;width:1200px;height:542px;background:linear-gradient(180deg,#5a5e63 0%,#3d4146 55%,#2b2e32 100%)}
.hero-photo{left:0;top:0;width:1200px;height:542px;background:radial-gradient(ellipse at 50% 35%,rgba(150,140,130,.55),rgba(40,42,46,0) 65%)}
.brand-tag{left:141px;top:16px;display:flex;align-items:center;gap:8px;font-family:"Montserrat",Arial,sans-serif;font-weight:700;font-size:22px;color:var(--white)}
.brand-tag i{width:14px;height:14px;background:var(--green);display:block}
.topnav{right:141px;top:20px;display:flex;align-items:center;gap:26px;color:var(--white);font-family:"Montserrat",Arial,sans-serif;font-size:14px;font-weight:500}
.topnav span{display:flex;align-items:center;gap:8px}
.play{width:46px;height:46px;border-radius:50%;background:var(--cta);display:flex;align-items:center;justify-content:center}
.hero-title{left:0;top:262px;width:1200px;text-align:center;color:var(--white);font-family:"Montserrat",Arial,sans-serif;font-weight:500;font-size:29px;line-height:42px}

/* solutions */
.sol-card{top:748px;width:139px;height:184px;background:var(--light);display:flex;flex-direction:column;align-items:center;padding-top:34px}
.sol-card p{margin-top:18px;font-family:"Montserrat",Arial,sans-serif;font-weight:600;font-size:12px;line-height:16px;text-align:center;color:var(--charcoal)}

/* webinar */
.webinar{left:0;top:983px;width:1200px;height:367px;background:linear-gradient(180deg,#0f1a2c 0%,#1d2c47 55%,#2d2a2a 100%)}
.video{left:141px;top:1034px;width:390px;height:266px;background:var(--light)}
.video-brand{left:0;top:54px;width:390px;text-align:center;font-family:"Montserrat",Arial,sans-serif;font-weight:700;font-size:30px;color:var(--green)}
.video-tag{left:0;top:104px;width:390px;text-align:center;font-family:"Montserrat",Arial,sans-serif;font-weight:700;font-size:13px;color:var(--charcoal);letter-spacing:.5px}
.video-bar{left:0;bottom:0;width:390px;height:30px;background:#222}
.web-title{left:576px;top:1053px;font-family:"Montserrat",Arial,sans-serif;font-size:30px;font-weight:500;color:var(--white)}
.web-copy{left:576px;top:1118px;width:520px;font-size:11.5px;line-height:19px;color:var(--white)}
.web-input{left:576px;top:1183px;width:390px;height:32px;background:var(--white);font-size:12px;color:var(--text);padding:0 12px;display:flex;align-items:center}

/* case studies */
.case-logo{display:flex;align-items:center;gap:8px;font-family:"Montserrat",Arial,sans-serif;font-weight:700;color:var(--charcoal)}
.case-text{font-size:11.5px;line-height:20px;color:var(--text)}
.case-row{display:flex;justify-content:space-between;align-items:flex-start;gap:16px}
.stat{background:var(--charcoal);color:var(--white);font-size:11px;font-weight:600;padding:2px 8px;min-width:62px;text-align:center;flex:none}
.quote{color:var(--muted)}
.author b{color:var(--cta);font-weight:600}
.chart{background:var(--white);border:1px solid #cfcfcf;box-shadow:0 2px 6px rgba(0,0,0,.12)}

/* clients */
.clients{left:0;top:2485px;width:1200px;height:466px;background:var(--light)}
.client{width:133px;height:68px;background:var(--white);display:flex;align-items:center;justify-content:center;font-family:"Montserrat",Arial,sans-serif;font-weight:700;font-size:12.5px;color:var(--charcoal);text-align:center;box-shadow:0 1px 3px rgba(0,0,0,.08)}

/* blog */
.post{top:3084px;width:452px;height:271px;color:var(--white)}
.post .date{position:absolute;left:18px;top:10px;font-family:"Montserrat",Arial,sans-serif}
.post .date b{font-size:30px;font-weight:500;display:block;line-height:34px}
.post .date span{font-size:12px}
.post h3{position:absolute;left:18px;top:192px;font-family:"Montserrat",Arial,sans-serif;font-size:13px;font-weight:500}
.post p{position:absolute;left:18px;top:214px;width:400px;font-size:9.5px;line-height:14px}

/* learning & media */
.divider{left:0;top:3403px;width:1200px;height:16px;background:var(--light)}
.conf{top:3592px;width:136px;height:74px;background:var(--white);border:1px solid var(--line);display:flex;align-items:center;justify-content:center;font-family:"Montserrat",Arial,sans-serif;font-weight:700;font-size:15px;color:var(--charcoal)}
.media{top:3836px;width:180px;text-align:center;font-family:"Montserrat",Arial,sans-serif;color:var(--charcoal)}
.media b{display:block;font-size:24px;font-weight:700}
.media span{display:block;font-size:11px;color:var(--text);margin-top:6px}

/* footer */
.footer{left:0;top:3940px;width:1200px;height:295px;background:var(--charcoal);color:var(--white)}
.foot-h{font-family:"Montserrat",Arial,sans-serif;font-size:14px;font-weight:500;color:var(--white)}
.foot-list{font-size:11.5px;line-height:22px;color:#cfcfcf;list-style:none}
.foot-list li::before{content:"•";margin-right:6px;color:#cfcfcf}
.foot-list li.on{color:var(--green)}
.social{display:flex;flex-wrap:wrap;gap:8px 14px;width:220px;font-size:11px;color:#cfcfcf}
.social span{display:flex;align-items:center;gap:5px}
.social i{display:block;width:10px;height:10px;background:var(--cta)}
.affiliate{left:655px;top:4067px;width:145px;height:70px;background:var(--white);border-radius:3px}
.affiliate::before{content:"";position:absolute;left:0;top:0;width:18px;height:70px;background:var(--green);border-radius:3px 0 0 3px}
.foot-brand{left:861px;top:4064px;display:flex;align-items:center;gap:8px;font-family:"Montserrat",Arial,sans-serif;font-weight:700;font-size:22px;color:var(--white)}
.foot-brand i{width:14px;height:14px;background:var(--green);display:block}
.copyright{left:0;top:4180px;width:1200px;height:55px;background:#0d0d0d;display:flex;align-items:center;justify-content:center;font-size:11.5px;color:var(--green)}
</style>
</head>
<body>

<!-- HERO -->
<section class="abs hero" aria-label="Hero">
  <div class="abs hero-photo" role="img" aria-label="Photo of the BrightLoop team standing together"></div>
  <div class="abs brand-tag"><i></i>BrightLoop</div>
  <nav class="abs topnav">
    <span><svg width="14" height="14" viewBox="0 0 24 24" fill="#fff"><path d="M6.6 10.8a15.1 15.1 0 0 0 6.6 6.6l2.2-2.2c.3-.3.7-.4 1-.2 1.1.4 2.3.6 3.6.6.6 0 1 .4 1 1V20c0 .6-.4 1-1 1C10.6 21 3 13.4 3 4c0-.6.4-1 1-1h3.5c.6 0 1 .4 1 1 0 1.3.2 2.5.6 3.6.1.3 0 .7-.2 1z"/></svg>1300 555 019</span>
    <span>MENU <svg width="22" height="20" viewBox="0 0 22 20" fill="none" stroke="#fff" stroke-width="1.5"><rect x=".75" y=".75" width="20.5" height="18.5"/><path d="M5 6h12M5 10h12M5 14h12"/></svg></span>
  </nav>
  <div class="abs play" style="left:577px;top:192px"><svg width="16" height="18" viewBox="0 0 16 18"><path d="M2 1l13 8-13 8z" fill="#fff"/></svg></div>
  <h1 class="abs hero-title">We Help Smart Marketing Managers Achieve Their KPIs<br>And Reduce Their Digital Marketing Overwhelm.</h1>
  <a class="abs btn" style="left:530px;top:363px;width:140px;height:36px">Contact Us</a>
</section>

<!-- SOLUTIONS -->
<h2 class="abs heading" style="top:594px">OUR SOLUTIONS</h2>
<p class="abs lead" style="top:680px">Lorem ipsum dolor sit amet, consectetur adipiscing elit, sed do eiusmod tempor incididunt ut labore et dolore magna aliqua.</p>

<div class="abs sol-card" style="left:141px">
  <svg width="56" height="56" viewBox="0 0 56 56" fill="none" stroke="#161616" stroke-width="2"><path d="M6 50h44"/><rect x="10" y="34" width="7" height="16"/><rect x="22" y="26" width="7" height="24"/><rect x="34" y="16" width="7" height="34"/><path d="M8 28L22 16l8 6 16-14" stroke="#428e29"/><path d="M40 8h6v6" stroke="#428e29"/></svg>
  <p>Grow<br>Revenue</p>
</div>
<div class="abs sol-card" style="left:297px">
  <svg width="56" height="56" viewBox="0 0 56 56" fill="none" stroke="#161616" stroke-width="2"><path d="M8 10h40L32 30v16l-8 4V30z"/><path d="M14 18h28" stroke="#428e29"/></svg>
  <p>Convert<br>Leads</p>
</div>
<div class="abs sol-card" style="left:453px">
  <svg width="56" height="56" viewBox="0 0 56 56" fill="none" stroke="#161616" stroke-width="2"><rect x="10" y="6" width="32" height="42"/><path d="M16 16h20M16 24h20M16 32h12"/><circle cx="42" cy="42" r="8" stroke="#428e29"/><path d="M38 42l3 3 5-6" stroke="#428e29"/></svg>
  <p>Convert<br>Leads</p>
</div>
<div class="abs sol-card" style="left:609px">
  <svg width="56" height="56" viewBox="0 0 56 56" fill="none" stroke="#161616" stroke-width="2"><path d="M6 16l22-8 22 8-22 8z"/><path d="M6 24l22 8 22-8" stroke="#428e29"/><path d="M6 32l22 8 22-8"/><path d="M6 40l22 8 22-8"/></svg>
  <p>Data /<br>KPI's</p>
</div>
<div class="abs sol-card" style="left:765px">
  <svg width="56" height="56" viewBox="0 0 56 56" fill="none" stroke="#161616" stroke-width="2"><circle cx="16" cy="16" r="6"/><circle cx="40" cy="16" r="6"/><path d="M6 36c0-6 4-10 10-10s10 4 10 10M30 36c0-6 4-10 10-10s10 4 10 10"/><path d="M6 44h44" stroke="#428e29"/><path d="M24 50h8" stroke="#428e29"/></svg>
  <p>Increase<br>Engagement</p>
</div>
<div class="abs sol-card" style="left:921px">
  <svg width="56" height="56" viewBox="0 0 56 56" fill="none" stroke="#161616" stroke-width="2"><rect x="12" y="8" width="32" height="42"/><rect x="22" y="4" width="12" height="8"/><path d="M18 22l3 3 5-6M18 34l3 3 5-6" stroke="#428e29"/><path d="M30 22h8M30 34h8"/></svg>
  <p>Marketing Strategy<br>/ Budgeting</p>
</div>

<!-- WEBINAR -->
<section class="abs webinar" role="img" aria-label="Night city harbour skyline behind the webinar section"></section>
<div class="abs video">
  <div class="abs video-brand">BrightLoop</div>
  <div class="abs video-tag">ACHIEVE YOUR <span style="color:var(--cta)">REVENUE</span> TARGETS</div>
  <div class="abs play" style="left:177px;top:130px;width:38px;height:38px"><svg width="13" height="15" viewBox="0 0 16 18"><path d="M2 1l13 8-13 8z" fill="#fff"/></svg></div>
  <div class="abs video-bar">
    <svg width="390" height="30" viewBox="0 0 390 30"><rect x="12" y="10" width="3" height="10" fill="#fff"/><rect x="18" y="10" width="3" height="10" fill="#fff"/><rect x="40" y="14" width="290" height="3" fill="#555"/><rect x="40" y="14" width="70" height="3" fill="var(--green)"/><circle cx="110" cy="15.5" r="5" fill="#fff"/><path d="M350 12h4l5-4v14l-5-4h-4z" fill="#fff"/></svg>
  </div>
</div>
<h2 class="abs web-title">REGISTER FREE WEBINAR</h2>
<p class="abs web-copy">Lorem ipsum dolor sit amet, consectetur adipiscing elit, sed diam nonummy nibh euismod tincidunt ut laoreet dolore magna aliquam erat volutpat.</p>
<div class="abs web-input">Enter Your Email Address</div>
<a class="abs btn" style="left:576px;top:1237px;width:134px;height:34px;border-radius:3px">Register Now</a>

<!-- CASE STUDIES -->
<h2 class="abs heading" style="top:1401px">CASE STUDIES</h2>

<!-- case 1 -->
<div class="abs case-logo" style="left:141px;top:1491px;width:212px;height:62px;background:var(--light);justify-content:center;font-size:20px"><i style="display:block;width:14px;height:14px;background:var(--cta)"></i>Keldon Storage</div>
<div class="abs case-text" style="left:141px;top:1578px;width:450px">
  <div class="case-row"><span>From 2014 – 2017 we saw a major increase in organic conversions</span><span class="stat">500%</span></div>
  <div class="case-row" style="margin-top:6px"><span>From 2014 – 2017 we saw a significant increase in organic traffic</span><span class="stat">153%</span></div>
  <p class="quote">"I'm pleased to report we're now on page 1 and that was through the advice and help given to us by BrightLoop."</p>
  <p class="author"><b>Dean Maller</b> – General Manager</p>
</div>
<a class="abs btn" style="left:141px;top:1730px;width:100px;height:26px">Read More</a>
<svg class="abs chart" style="left:635px;top:1491px" width="424" height="274" viewBox="0 0 424 274">
  <g stroke="#e2e2e2"><path d="M50 30h350M50 70h350M50 110h350M50 150h350M50 190h350M50 230h350"/></g>
  <path d="M50 30v200h350" stroke="#999" fill="none"/>
  <g font-size="9" fill="#333" font-family="Open Sans,sans-serif" text-anchor="end"><text x="44" y="33">1000</text><text x="44" y="73">800</text><text x="44" y="113">600</text><text x="44" y="153">400</text><text x="44" y="193">200</text><text x="44" y="233">0</text></g>
  <g font-size="9" fill="#333" font-family="Open Sans,sans-serif" text-anchor="middle"><text x="120" y="246">2</text><text x="190" y="246">4</text><text x="260" y="246">6</text><text x="330" y="246">8</text><text x="400" y="246">10</text></g>
  <polyline fill="none" stroke="#e53935" stroke-width="2" points="50,192 85,170 120,168 155,152 190,160 225,148 260,104 295,82 330,128 365,122 400,162"/>
  <g fill="#e53935"><circle cx="50" cy="192" r="2.5"/><circle cx="85" cy="170" r="2.5"/><circle cx="120" cy="168" r="2.5"/><circle cx="155" cy="152" r="2.5"/><circle cx="190" cy="160" r="2.5"/><circle cx="225" cy="148" r="2.5"/><circle cx="260" cy="104" r="2.5"/><circle cx="295" cy="82" r="2.5"/><circle cx="330" cy="128" r="2.5"/><circle cx="365" cy="122" r="2.5"/><circle cx="400" cy="162" r="2.5"/></g>
</svg>

<!-- case 2 -->
<svg class="abs chart" style="left:141px;top:1821px" width="424" height="283" viewBox="0 0 424 283">
  <g stroke="#cde3c5"><path d="M70 30v210M110 30v210M150 30v210M190 30v210M230 30v210M270 30v210M310 30v210M350 30v210M390 30v210M50 60h350M50 90h350M50 120h350M50 150h350M50 180h350M50 210h350"/></g>
  <path d="M50 30v210h350" stroke="#999" fill="none"/>
  <g font-size="9" fill="#333" font-family="Open Sans,sans-serif" text-anchor="end"><text x="44" y="33">100</text><text x="44" y="63">95</text><text x="44" y="93">90</text><text x="44" y="123">85</text><text x="44" y="153">80</text><text x="44" y="183">75</text><text x="44" y="213">70</text></g>
  <g font-size="9" fill="#333" font-family="Open Sans,sans-serif" text-anchor="middle"><text x="50" y="254">7</text><text x="120" y="254">8</text><text x="190" y="254">9</text><text x="260" y="254">10</text><text x="330" y="254">11</text><text x="400" y="254">12</text></g>
  <polyline fill="none" stroke="#2e9c3a" stroke-width="3" points="50,222 85,212 120,198 155,176 190,180 225,186 260,178 295,166 330,152 365,124 400,92"/>
  <g fill="#2e9c3a"><circle cx="50" cy="222" r="3"/><circle cx="120" cy="198" r="3"/><circle cx="190" cy="180" r="3"/><circle cx="260" cy="178" r="3"/><circle cx="330" cy="152" r="3"/><circle cx="400" cy="92" r="3"/></g>
</svg>
<div class="abs case-logo" style="left:604px;top:1821px;width:215px;height:57px;background:var(--charcoal);color:var(--white);justify-content:center;font-size:19px">homeseeker</div>
<div class="abs case-text" style="left:604px;top:1901px;width:455px">
  <div class="case-row"><span>From 2014 – 2017 we saw an impressive increase in organic traffic</span><span class="stat">123%</span></div>
  <div class="case-row" style="margin-top:6px"><span>Thanks to concerted conversion optimisation efforts we saw a huge increase in their primary form's conversion rate</span><span class="stat">363%</span></div>
  <p class="quote">"It's been totally essential. We wouldn't have the business today without digital marketing."</p>
  <p class="author"><b>Rory Hanlon</b> – Managing Director</p>
</div>
<a class="abs btn" style="left:604px;top:2069px;width:100px;height:26px">Read More</a>

<!-- case 3 -->
<div class="abs case-logo" style="left:141px;top:2155px;width:220px;height:53px;font-size:17px"><i style="display:block;width:14px;height:14px;border-radius:50%;background:var(--charcoal)"></i>clearview eye clinic</div>
<div class="abs case-text" style="left:141px;top:2228px;width:450px">
  <div class="case-row"><span>Organic traffic now makes up more than half of the total website traffic.</span><span class="stat">77%</span></div>
  <div class="case-row" style="margin-top:6px"><span>2014 – 2017 we saw a significant increase in organic traffic to the website.</span><span class="stat">154.87%</span></div>
  <p class="quote">"BrightLoop is proactive. You address things we haven't even thought about."</p>
</div>
<a class="abs btn" style="left:141px;top:2368px;width:100px;height:26px">Read More</a>
<svg class="abs chart" style="left:635px;top:2155px" width="424" height="279" viewBox="0 0 424 279">
  <g stroke="#e2e2e2"><path d="M40 30h360M40 70h360M40 110h360M40 150h360M40 190h360"/></g>
  <path d="M40 30v200h360" stroke="#999" fill="none"/>
  <g font-size="9" fill="#333" font-family="Open Sans,sans-serif" text-anchor="end"><text x="34" y="33">25</text><text x="34" y="73">20</text><text x="34" y="113">15</text><text x="34" y="153">10</text><text x="34" y="193">5</text></g>
  <g font-size="9" fill="#333" font-family="Open Sans,sans-serif" text-anchor="middle"><text x="40" y="246">1</text><text x="91" y="246">2</text><text x="143" y="246">3</text><text x="194" y="246">4</text><text x="246" y="246">5</text><text x="297" y="246">6</text><text x="349" y="246">7</text><text x="400" y="246">8</text></g>
  <polyline fill="none" stroke="#1e5bb8" stroke-width="2" points="40,186 66,176 91,170 117,176 143,184 168,164 194,152 220,168 246,166 271,140 297,126 323,154 349,172 374,116 400,80"/>
</svg>

<!-- CLIENTS -->
<section class="abs clients" aria-label="Clients"></section>
<h2 class="abs heading" style="top:2528px">OUR CLIENTS</h2>
<div class="abs client" style="left:141px;top:2618px">clearview</div>
<div class="abs client" style="left:298px;top:2618px">Marketing Geelong</div>
<div class="abs client" style="left:455px;top:2618px">The Fairmont Academy</div>
<div class="abs client" style="left:612px;top:2618px">corvane</div>
<div class="abs client" style="left:769px;top:2618px">Emberly Creative</div>
<div class="abs client" style="left:926px;top:2618px">Sleepwell Co</div>
<div class="abs client" style="left:141px;top:2717px">Keldon Storage</div>
<div class="abs client" style="left:298px;top:2717px">Stillwater</div>
<div class="abs client" style="left:455px;top:2717px">Ridgeline</div>
<div class="abs client" style="left:612px;top:2717px">BoxCraft</div>
<div class="abs client" style="left:769px;top:2717px">Exacto Solutions</div>
<div class="abs client" style="left:926px;top:2717px">Cottage Co</div>
<div class="abs client" style="left:141px;top:2815px">NK Strategy</div>
<div class="abs client" style="left:298px;top:2815px">page nation</div>
<div class="abs client" style="left:455px;top:2815px">Orbit Studio</div>
<div class="abs client" style="left:612px;top:2815px">Keystone Editing</div>
<div class="abs client" style="left:769px;top:2815px">Bramblers</div>
<div class="abs client" style="left:926px;top:2815px">QRT</div>

<!-- BLOG -->
<h2 class="abs heading" style="top:2988px">LATEST FROM BLOG</h2>
<article class="abs post" style="left:141px;background:linear-gradient(160deg,#8d8f92 0%,#5b5d60 55%,#2d2e30 100%)" role="img" aria-label="Photo of hands typing on a laptop showing a search page">
  <div class="date"><b>01</b><span>Feb</span></div>
  <h3>BUSINESS BLOG</h3>
  <p>Brands have added a new feature to their search results which lists positively reviewed products upon a query looking for "the best" of something... [+]</p>
</article>
<article class="abs post" style="left:607px;background:linear-gradient(160deg,#2f6f7a 0%,#3e8c86 50%,#1f3f46 100%)" role="img" aria-label="Photo of coloured kettlebells on a gym floor">
  <div class="date"><b>01</b><span>Feb</span></div>
  <h3>CULTURE BLOG</h3>
  <p>Brands have added a new feature to their search results which lists positively reviewed products upon a query looking for "the best" of something... [+]</p>
</article>

<!-- LEARNING -->
<div class="abs divider"></div>
<h2 class="abs heading" style="top:3452px">LEARNING</h2>
<p class="abs lead" style="top:3530px">Lorem ipsum dolor sit amet, consectetur adipiscing elit, sed do eiusmod tempor incididunt ut labore et dolore magna aliqua.</p>
<div class="abs conf" style="left:192px">MOTECON</div>
<div class="abs conf" style="left:362px">SRX</div>
<div class="abs conf" style="left:532px">POSTCON</div>
<div class="abs conf" style="left:702px">Pagelift</div>
<div class="abs conf" style="left:872px">INFLOW</div>

<!-- MEDIA -->
<h2 class="abs heading" style="top:3757px">IN THE MEDIA</h2>
<div class="abs media" style="left:110px"><b>Pagelift</b><span>Seattle – 2016</span></div>
<div class="abs media" style="left:310px"><b>POSTCON</b><span>Las Vegas – 2017, 2016</span></div>
<div class="abs media" style="left:510px"><b>MOTECON</b><span>Seattle – 2015, 2013</span></div>
<div class="abs media" style="left:710px"><b>ApexConf</b><span>Austin – 2013</span></div>
<div class="abs media" style="left:910px"><b>SRX</b><span>Sydney, Melbourne – 2015, 2014</span></div>

<!-- FOOTER -->
<footer class="abs footer"></footer>
<h4 class="abs foot-h" style="left:141px;top:3986px">Navigation</h4>
<ul class="abs foot-list" style="left:141px;top:4012px">
  <li class="on">Home</li><li>About</li><li>PPC</li><li>SEO</li><li>Training</li>
</ul>
<ul class="abs foot-list" style="left:225px;top:4012px">
  <li>Client Success</li><li>Blog</li><li>Resources</li><li>Contact</li>
</ul>
<h4 class="abs foot-h" style="left:367px;top:3986px">Contact Details</h4>
<div class="abs foot-list" style="left:367px;top:4012px;width:220px;line-height:18px">
  <div style="color:var(--green)">BrightLoop Digital Marketing</div>
  <div>24 Harbour Lane, Millers Point, Sydney,<br>NSW</div>
  <div style="margin-top:10px;display:flex;align-items:center;gap:6px"><svg width="11" height="11" viewBox="0 0 24 24" fill="#cfcfcf"><path d="M6.6 10.8a15.1 15.1 0 0 0 6.6 6.6l2.2-2.2c.3-.3.7-.4 1-.2 1.1.4 2.3.6 3.6.6.6 0 1 .4 1 1V20c0 .6-.4 1-1 1C10.6 21 3 13.4 3 4c0-.6.4-1 1-1h3.5c.6 0 1 .4 1 1 0 1.3.2 2.5.6 3.6.1.3 0 .7-.2 1z"/></svg>1300 555 019</div>
  <div style="margin-top:8px;display:flex;align-items:center;gap:6px"><svg width="12" height="10" viewBox="0 0 24 18" fill="none" stroke="#cfcfcf" stroke-width="2"><rect x="1" y="1" width="22" height="16"/><path d="M1 1l11 9 11-9"/></svg>info@brightloop.example.au</div>
</div>
<h4 class="abs foot-h" style="left:627px;top:3986px">Follow Us</h4>
<div class="abs social" style="left:627px;top:4014px">
  <span><i></i>WorkMesh</span><span><i></i>Blipster</span><span><i></i>Pallwall</span><span><i></i>ReelDrop</span><span><i></i>Zentro Hub</span>
</div>
<div class="abs affiliate" role="img" aria-label="Zentro honoured affiliate badge"></div>
<div class="abs foot-brand"><i></i>BrightLoop</div>
<div class="abs copyright">© BrightLoop Digital Marketing – 2018. All Rights Reserved</div>

</body>
</html>
```